New Business Card Design Project

Easy part first... I want the backside to be simple... jet black background with our logo in jet black/white/color. Feel free to play with tagline ideas under the logo if you want, I'm still toying around with it myself.

The front side... I need the logo on it, my photo headshot, and the following information:

Ray T. Calloway
Top Producer
555-201-4837
calloway.ray.t@fernmail.example
www.listnorthernnests.example
www.getnorthernnests.example

I'm looking for creativity with font, simple, but elegant, pairs well with the logo, good visibility of my photo, black background on the front as well, clearly see and identify information.
Updates

I would like the websites to have capitalization on the first letter of each word - www.ListNorthernNests.example and www.GetNorthernNests.example Also, I would like each of the capital letters to be slightly larger than the other font

Target Market(s)

We help people buy and sell homes from $50,000 to over a $1million.

Industry/Entity Type

Business

Requirements
Must have
• Must have information from above.
Nice to have
• Introducing a new color to be sharp against the black- possibly in the silver/nickel/platinum metallics? Feel free to crop the headshot down some if needed.
Should not have
• NO CHEESY GRAPHICS

```html
<!DOCTYPE html>
<html lang="en">
<head>
<meta charset="utf-8">
<title>Northern Nests Realty — Business Card</title>
<link rel="stylesheet" href="https://fonts.googleapis.com/css2?family=Noticia+Text:wght@400;700&family=Arimo:wght@400&display=swap">
<style>
  :root {
    --page: #d8d3ca;
    --card-black: #0b0b0b;
    --card-black-soft: #1a1a1a;
    --gold: #b9a97c;
    --white: #f4f4f2;
    --band-grey: #e3e3e5;
    --ink: #151515;
    --photo-dark: #202225;
    --photo-mid: #3a3d44;
  }
  * { margin: 0; padding: 0; box-sizing: border-box; }
  html, body {
    width: 1200px;
    height: 1023px;
    overflow: hidden;
    background: var(--page);
  }
  .stage {
    position: relative;
    width: 1200px;
    height: 1023px;
  }
  .card {
    position: absolute;
    width: 540px;
    height: 309px;
    background: var(--card-black);
    overflow: hidden;
    box-shadow: 0 14px 30px rgba(0,0,0,0.28);
  }
  .card--front { left: 60px; top: 150px; }
  .card--back {
    left: 600px; top: 560px;
    background: linear-gradient(160deg, var(--card-black-soft) 0%, var(--card-black) 55%);
    display: flex;
    align-items: center;
    justify-content: center;
  }

  /* headshot area */
  .headshot {
    position: absolute;
    right: 0;
    top: 0;
    width: 300px;
    height: 196px;
    background: radial-gradient(circle at 40% 35%, var(--photo-mid) 0%, var(--photo-dark) 60%, var(--card-black) 100%);
  }

  /* wordmark */
  .wordmark {
    display: flex;
    align-items: center;
    gap: 10px;
  }
  .wordmark__square {
    width: 16px;
    height: 16px;
    background: var(--gold);
    flex: none;
  }
  .wordmark__name {
    font-family: "Noticia Text", Georgia, serif;
    font-weight: 400;
    color: var(--white);
    text-transform: uppercase;
    letter-spacing: 0.06em;
    line-height: 1.15;
  }
  .card--front .wordmark {
    position: absolute;
    left: 34px;
    top: 118px;
  }
  .card--front .wordmark__name { font-size: 14px; }
  .card--back .wordmark { gap: 14px; }
  .card--back .wordmark__square { width: 24px; height: 24px; }
  .card--back .wordmark__name { font-size: 24px; }

  /* agent */
  .agent {
    position: absolute;
    left: 34px;
    top: 186px;
  }
  .agent__name {
    font-family: "Noticia Text", Georgia, serif;
    font-weight: 700;
    font-size: 17px;
    color: var(--gold);
  }
  .agent__title {
    font-family: "Arimo", Arial, sans-serif;
    font-size: 13px;
    color: var(--white);
    margin-top: 2px;
  }

  /* contact band */
  .contact {
    position: absolute;
    right: 0;
    bottom: 0;
    width: 300px;
    height: 113px;
    background: var(--band-grey);
    padding: 14px 0 0 22px;
    list-style: none;
  }
  .contact__item {
    display: flex;
    align-items: center;
    gap: 8px;
    font-family: "Arimo", Arial, sans-serif;
    font-size: 12.5px;
    color: var(--ink);
    height: 21px;
  }
  .contact__icon { width: 11px; height: 11px; flex: none; }
</style>
</head>
<body>
<main class="stage">

  <section class="card card--front" aria-label="Card front">
    <div class="headshot" role="img" aria-label="Headshot of Ray T. Calloway in dark suit and blue tie"></div>

    <div class="wordmark">
      <span class="wordmark__square"></span>
      <span class="wordmark__name">Northern Nests<br>Realty</span>
    </div>

    <div class="agent">
      <p class="agent__name">Ray T. Calloway</p>
      <p class="agent__title">Top Producer</p>
    </div>

    <ul class="contact">
      <li class="contact__item">
        <svg class="contact__icon" viewBox="0 0 12 12" aria-hidden="true"><path d="M2.5 1 L4.5 1 L5.2 3.6 L4 4.6 Q5 7 7.4 8 L8.4 6.8 L11 7.5 L11 9.5 Q10.5 11 9 11 Q1 10 1 3 Q1 1.5 2.5 1 Z" fill="var(--ink)"/></svg>
        555-201-4837
      </li>
      <li class="contact__item">
        <svg class="contact__icon" viewBox="0 0 12 12" aria-hidden="true"><rect x="0.5" y="2.5" width="11" height="7.5" fill="var(--ink)"/><path d="M0.5 2.5 L6 7 L11.5 2.5" stroke="var(--band-grey)" stroke-width="1" fill="none"/></svg>
        calloway.ray.t@fernmail.example
      </li>
      <li class="contact__item">
        <svg class="contact__icon" viewBox="0 0 12 12" aria-hidden="true"><circle cx="6" cy="6" r="5.5" fill="var(--ink)"/><path d="M0.5 6 H11.5 M6 0.5 V11.5" stroke="var(--band-grey)" stroke-width="0.9"/><ellipse cx="6" cy="6" rx="2.4" ry="5.5" stroke="var(--band-grey)" stroke-width="0.9" fill="none"/></svg>
        www.listnorthernnests.example
      </li>
      <li class="contact__item">
        <svg class="contact__icon" viewBox="0 0 12 12" aria-hidden="true"><circle cx="6" cy="6" r="5.5" fill="var(--ink)"/><path d="M0.5 6 H11.5 M6 0.5 V11.5" stroke="var(--band-grey)" stroke-width="0.9"/><ellipse cx="6" cy="6" rx="2.4" ry="5.5" stroke="var(--band-grey)" stroke-width="0.9" fill="none"/></svg>
        www.getnorthernnests.example
      </li>
    </ul>
  </section>

  <section class="card card--back" aria-label="Card back">
    <div class="wordmark">
      <span class="wordmark__square"></span>
      <span class="wordmark__name">Northern Nests<br>Realty</span>
    </div>
  </section>

</main>
</body>
</html>
```